120ml Jar Label — Masculine Cosmetic Foot Balm for Cracked, Hardworking Heels

We need a print-ready wraparound label for a 120ml jar — a brown/amber glass jar with a black metal screw lid (file photo attached).

--DO NOT PUT A BARCODE ON THE LABEL PLEASE--
**PLEASE READ "PLAN HUDDLE PROJECT BRIEF FINAL.MD" IN ATTACHED FILES IF YOU ARE SUBMITTING A DESIGN.**

The label is 190mm wide × 40mm high.
We need files to be in an .ai format with a 2mm bleed at the end.
Social media handle: @bramblekeepnz (facebook, instagram and tiktok)

Bramble Keep is a New Zealand foot-care brand making practical, no-nonsense products for hardworking men whose jobs wreck their feet. Our flagship product, Ridge Mender Balm, helps fix thick, cracked, hardworking skin.

Brand color scheme and overview is all in the brief file. You may add some brand aligned colors outside of the specified hex codes as you see fit to make a great design. Feel free to remove the "Bramble Keep" text from the logo so Bramble Keep is not doubled up on the front of the label

The tone we want: direct, rugged, and credible — like a workwear brand, not a spa brand. Most cracked-heel products on the market lean soft and feminine; we want to stand apart by looking like a serious fix for a real problem, made in New Zealand.

Full legal requirements for New Zealand cosmetic labelling (ingredients, directions, net contents, origin, etc.) are listed in the attached brief document — these are non-negotiable and must stay legible.

Please see the label attached "Label spacing guide" for this project's rough spacing guide. This label is the same size and sits well on the jar. This label doesn't need to be spaced quite as much as the Verin Label

I want to run the design for a week - I feel 7 days is a good amount of time for designers to see the work, digest the brief and create something remarkable and memorable for Bramble Keep.

Target Market(s)

Working men in New Zealand whose jobs or lifestyle put heavy wear on their feet — tradies, farmers, hospital/shift workers, hunters, and outdoors people. Practical, value-driven buyers rather than luxury skincare shoppers.

Industry/Entity Type

Beauty / Health & Wellness / Cosmetics

Font styles to use
Sans Serif
Other font styles liked:
• Montserrat (bold, headings), Inter (regular, body)

Colors
00AB8E
00BBA5
67D7C9
C6EFE9
E9F9F6
FFC000
F8CF3A
FAE287
FDF2CF
FEFAEE

Requirements
Must have
• All NZ cosmetic labelling requirements from the attached brief (product name, tag line, net contents, ingredients, directions, storage, made in NZ) — legible and complete, not omitted for aesthetics Fits 190mm × 40mm wraparound format for a 120ml brown jar with black lid Uses our existing brand colors: Deep Olive #3C4A34, Bone White #F4EFE6, Terracotta Clay #C1683D, and Warm Grey #4A4540 (exact palette in attached brief) Uses Montserrat (headings) and Inter (body) or close equivalents Incorporates our existing shield-and-wing logo (attached) Brand name and product name clearly readable from a normal shelf/bathroom-cabinet distance
Nice to have
• A style that could extend into a hero/product photo later, similar to the NZ-hills-backdrop look on our website (screenshot attached) — not required for the label itself, just good to keep in mind Original icon work (e.g. a small soak/apply/sock icon set) if it fits the rugged brand feel A design that could work as a small back-label/wraparound split if the front can't fit everything at a readable size
Should not have
• No pastel colors, floral motifs, or delicate script fonts — this should never look like spa/luxury skincare. Don't introduce new brand colors outside the palette provided other than black.

```html
<!DOCTYPE html>
<html lang="en">
<head>
<meta charset="utf-8">
<title>Bramble Keep – Ridge Mender Balm Jar Label</title>
<link rel="stylesheet" href="https://fonts.googleapis.com/css2?family=Barlow+Semi+Condensed:wght@600;700;800&family=Inter:wght@400;500&display=swap">
<style>
  :root {
    --olive: #37472f;
    --olive-deep: #2f3d28;
    --bone: #f1e8d8;
    --terracotta: #c1683d;
    --ink: #222;
    --page: #ffffff;
  }
  * { box-sizing: border-box; margin: 0; padding: 0; }
  html, body {
    width: 1050px; height: 1200px; overflow: hidden;
    background: var(--page);
  }
  .canvas { position: relative; width: 1050px; height: 1200px; }

  /* Dimension guides */
  .dims { position: absolute; inset: 0; pointer-events: none; }
  .dim-label {
    position: absolute; font-family: "Inter", sans-serif; font-size: 19px; color: var(--ink);
  }
  .dim-width { left: 500px; top: 38px; }
  .dim-height { left: 10px; top: 320px; transform: rotate(-90deg); transform-origin: left top; }

  /* Label panels */
  .label {
    position: absolute; left: 79px; width: 919px;
    background: var(--olive); color: var(--bone);
  }
  .label-front { top: 93px; height: 487px; }
  .label-back { top: 626px; height: 517px; }
  .frame { position: absolute; inset: 0; }

  .heading {
    font-family: "Barlow Semi Condensed", sans-serif; font-weight: 700;
    text-transform: uppercase; letter-spacing: 0.2px; color: var(--bone);
  }
  .body-text {
    font-family: "Inter", sans-serif; font-weight: 400; color: var(--bone);
    font-size: 15px; line-height: 18.5px;
  }

  /* Front: claims */
  .claims {
    position: absolute; left: 120px; top: 266px; width: 235px;
    list-style: none; text-align: center;
  }
  .claims li { font-size: 21px; line-height: 44px; }
  .claims { top: 158px; }

  /* Front: brand */
  .brand-mark {
    position: absolute; left: 345px; top: 100px; width: 180px; height: 180px;
  }
  .brand-name {
    position: absolute; left: 250px; top: 336px; width: 370px; text-align: center;
  }
  .brand-name .name { display: block; font-size: 50px; line-height: 52px; font-weight: 800; }
  .brand-name .region { display: block; font-size: 27px; line-height: 34px; font-weight: 700; }

  /* Front: product */
  .product {
    position: absolute; left: 665px; top: 154px; width: 182px; text-align: center;
  }
  .product .rule { height: 3px; background: var(--terracotta); }
  .product-name { font-size: 46px; line-height: 46px; font-weight: 800; margin-top: 12px; }
  .tagline { font-size: 20px; line-height: 24px; margin: 10px 0 14px; }
  .net { font-family: "Inter", sans-serif; font-size: 20px; margin-top: 20px; }

  /* Back columns */
  .col { position: absolute; top: 60px; }
  .col-info { left: 57px; width: 260px; }
  .col-usage { left: 360px; width: 245px; }
  .col-care { left: 644px; width: 225px; }
  .col .heading { font-size: 20px; line-height: 24px; margin-bottom: 2px; }
  .section { margin-bottom: 22px; }
  .section.tight { margin-bottom: 14px; }
  .divider { height: 2px; background: var(--terracotta); }
  .col-info .divider { position: absolute; top: 268px; width: 250px; }

  .back-claims { position: absolute; left: 57px; top: 364px; list-style: none; }
  .back-claims li { font-size: 20px; line-height: 25.5px; }
  .back-claims li::before {
    content: ""; display: inline-block; width: 14px; height: 2px;
    background: var(--terracotta); vertical-align: middle; margin-right: 10px;
  }

  .social {
    display: flex; align-items: center; gap: 8px; margin-top: 16px;
    font-family: "Inter", sans-serif; font-size: 16px;
  }
  .social .dot { width: 14px; height: 14px; border: 2px solid var(--bone); border-radius: 3px; }
  .icon-set { display: flex; gap: 20px; margin-top: 14px; }
  .icon-slot {
    width: 58px; height: 56px; border-radius: 6px;
    background: linear-gradient(180deg, rgba(241,232,216,0.22), rgba(241,232,216,0.1));
  }
</style>
</head>
<body>
<div class="canvas">

  <svg class="dims" width="1050" height="1200" viewBox="0 0 1050 1200" aria-hidden="true">
    <g stroke="#222" stroke-width="1.3" fill="none">
      <line x1="89" y1="68" x2="988" y2="68"/>
      <polyline points="99,62 89,68 99,74"/>
      <polyline points="978,62 988,68 978,74"/>
      <line x1="89" y1="56" x2="89" y2="80"/>
      <line x1="988" y1="56" x2="988" y2="80"/>
      <line x1="52" y1="104" x2="52" y2="570"/>
      <polyline points="46,114 52,104 58,114"/>
      <polyline points="46,560 52,570 58,560"/>
      <line x1="40" y1="104" x2="70" y2="104"/>
      <line x1="40" y1="570" x2="70" y2="570"/>
      <line x1="1003" y1="104" x2="1022" y2="104"/>
      <line x1="1003" y1="570" x2="1022" y2="570"/>
      <line x1="89" y1="590" x2="89" y2="615"/>
      <line x1="988" y1="590" x2="988" y2="615"/>
      <line x1="50" y1="638" x2="70" y2="638"/>
      <line x1="1003" y1="638" x2="1022" y2="638"/>
      <line x1="50" y1="1133" x2="70" y2="1133"/>
      <line x1="1003" y1="1133" x2="1022" y2="1133"/>
      <line x1="89" y1="1155" x2="89" y2="1180"/>
      <line x1="988" y1="1155" x2="988" y2="1180"/>
    </g>
  </svg>
  <span class="dim-label dim-width">190mm</span>
  <span class="dim-label dim-height">40mm</span>

  <!-- Front label -->
  <section class="label label-front">
    <svg class="frame" width="919" height="487" viewBox="0 0 919 487" aria-hidden="true">
      <g stroke="#c1683d" fill="none">
        <rect x="12" y="12" width="895" height="463" stroke-width="1.5"/>
        <line x1="62" y1="30" x2="857" y2="30" stroke-width="2"/>
        <line x1="62" y1="457" x2="857" y2="457" stroke-width="2"/>
        <line x1="30" y1="62" x2="30" y2="425" stroke-width="2"/>
        <line x1="889" y1="62" x2="889" y2="425" stroke-width="2"/>
        <polyline points="30,50 30,30 50,30" stroke-width="2"/>
        <polyline points="869,30 889,30 889,50" stroke-width="2"/>
        <polyline points="30,437 30,457 50,457" stroke-width="2"/>
        <polyline points="869,457 889,457 889,437" stroke-width="2"/>
      </g>
    </svg>

    <ul class="claims heading">
      <li>Deep Repair</li>
      <li>Fast Absorbing</li>
      <li>Tough on Cracks</li>
      <li>Made in New Zealand</li>
    </ul>

    <svg class="brand-mark" viewBox="0 0 180 180" role="img" aria-label="Bramble Keep brand mark">
      <circle cx="90" cy="90" r="82" fill="#c1683d"/>
    </svg>

    <h1 class="brand-name heading">
      <span class="name">Bramble Keep</span>
      <span class="region">NZ</span>
    </h1>

    <div class="product">
      <div class="rule"></div>
      <h2 class="product-name heading">Ridge<br>Mender<br>Balm</h2>
      <p class="tagline body-text">Built for<br>Hardworking Feet</p>
      <div class="rule"></div>
      <p class="net">120ml</p>
    </div>
  </section>

  <!-- Back label -->
  <section class="label label-back">
    <svg class="frame" width="919" height="517" viewBox="0 0 919 517" aria-hidden="true">
      <rect x="10" y="10" width="899" height="497" fill="none" stroke="#c1683d" stroke-width="1.5"/>
    </svg>

    <div class="col col-info">
      <div class="section">
        <h3 class="heading">Product Description</h3>
        <p class="body-text">This balm is a heavy-duty formula made for feet that live in work boots. Built for long shifts, rough ground, heavy industrial and premium workwear.</p>
      </div>
      <div class="section">
        <h3 class="heading">Directions</h3>
        <p class="body-text">Apply a small amount to clean feet, working into the heel and other heavy-duty areas.</p>
      </div>
      <div class="divider"></div>
    </div>

    <ul class="back-claims heading">
      <li>Deep Repair</li>
      <li>Fast Absorbing</li>
      <li>Tough on Cracks</li>
      <li>Made in New Zealand</li>
    </ul>

    <div class="col col-usage">
      <div class="section">
        <h3 class="heading">Directions</h3>
        <p class="body-text">Apply to clean feet and massage in until absorbed.</p>
      </div>
      <div class="section">
        <h3 class="heading">Ingredients</h3>
        <p class="body-text">New Zealand Manuka honey, Beeswax, Essential oils, Shea butter, Coconut oil, Kawakawa extract, Spring water, Vitamin E, Lanolin and essential oils.</p>
      </div>
      <div class="section">
        <h3 class="heading">Made in New Zealand</h3>
      </div>
      <div class="section">
        <h3 class="heading">Manufacturer Details</h3>
        <p class="body-text">41 Kowhai Road,<br>Ashgrove, NZ 7400<br>(03) 555-0142<br>Contact: @bramblekeep.nz</p>
      </div>
    </div>

    <div class="col col-care">
      <div class="section">
        <h3 class="heading">Storage Instructions</h3>
        <p class="body-text">Store in a cool,<br>dry place.</p>
      </div>
      <div class="section tight">
        <h3 class="heading">Warnings</h3>
        <p class="body-text">For external use only. Avoid use on broken skin.</p>
      </div>
      <div class="section">
        <h3 class="heading">Made in New Zealand</h3>
        <p class="body-text">Made in New Zealand.<br>12 Totara Street,<br>Fernlea, NZ 7402<br>Contact us bramblekeep nz</p>
      </div>
      <div class="divider"></div>
      <div class="social">
        <span class="dot"></span>
        <span>@bramblekeepnz</span>
      </div>
      <div class="icon-set">
        <div class="icon-slot" role="img" aria-label="Line icon of a bare foot"></div>
        <div class="icon-slot" role="img" aria-label="Line icon of a protective shield"></div>
        <div class="icon-slot" role="img" aria-label="Line icon of a sock with a tick"></div>
      </div>
    </div>
  </section>

</div>
</body>
</html>
```